New website template

Create a new website template based on original logo and company vision.

The ideal outcome would be a PSD containing a home page and a content page.

The domain name is maple-ridge-ventures.co.uk and as you can see currently has a really simple holding page.

The company specialise in commercial property project management and have over 25 years experience in doing so.

Their logo is really simple, it would be nice to keep their site simple, clean, fresh and friendly.

We're planning to use bootstrap to ensure the site works nicely on a mobile device so it would be good if this could be kept in mind when designing the site.

Target Market(s)

commercial property sector.

Industry/Entity Type

It Company

Number of Pages Required

2 page

Font styles to use
Sans Serif

Colors
fece3e

Requirements
Must have
• a home page and a content page.
• bootstrap must be kept in mind when doing the design
• clean, fresh and professional
Should not have
• cartoon graphics.

```html
<!DOCTYPE html>
<html lang="en">
<head>
<meta charset="utf-8">
<title>Maple Ridge Ventures Ltd.</title>
<link href="https://fonts.googleapis.com/css2?family=Open+Sans:wght@400;600;700&family=Arimo:wght@400;700&display=swap" rel="stylesheet">
<style>
  :root {
    --brand-yellow: #f5ee6e;
    --brand-blue: #0b4a94;
    --ink: #1a1a1a;
    --ink-soft: #333333;
    --page-grey: #ececec;
    --panel-white: #ffffff;
    --rule: #c9c9c9;
    --overlay: rgba(60, 60, 60, 0.72);
  }
  * { box-sizing: border-box; margin: 0; padding: 0; }
  html, body { width: 1200px; height: 876px; overflow: hidden; }
  body {
    position: relative;
    background: var(--page-grey);
    font-family: "Arimo", Arial, sans-serif;
    color: var(--ink);
  }
  a { color: inherit; text-decoration: none; }

  /* Header */
  .site-header {
    position: absolute; left: 0; top: 0; width: 1200px; height: 105px;
    background: linear-gradient(#ffffff, #f3f3f3);
    box-shadow: 0 2px 5px rgba(0,0,0,0.35);
    z-index: 2;
  }
  .brand {
    position: absolute; left: 112px; top: 22px;
    display: flex; align-items: center; gap: 9px;
    font-family: "Open Sans", sans-serif; font-size: 30px; color: var(--ink);
  }
  .brand-square {
    width: 61px; height: 61px; background: var(--brand-yellow);
  }
  .call-now {
    position: absolute; right: 102px; top: 12px;
    font-family: "Open Sans", sans-serif; font-size: 18px; color: var(--ink);
  }
  .call-now strong { font-size: 30px; font-weight: 700; }
  .main-nav {
    position: absolute; right: 101px; top: 57px;
    display: flex; align-items: center; gap: 0;
    font-family: "Open Sans", sans-serif; font-size: 14px;
  }
  .main-nav a { padding: 6px 0; margin-left: 28px; }
  .main-nav a.is-active {
    margin-left: 0; padding: 5px 9px;
    background: var(--brand-yellow); border: 1px solid var(--ink);
    box-shadow: inset 0 0 0 2px var(--brand-yellow), inset 0 0 0 3px #fff;
    font-weight: 700;
  }

  /* Hero */
  .hero-photo {
    position: absolute; left: 0; top: 105px; width: 1200px; height: 610px;
    background:
      linear-gradient(90deg, rgba(0,0,0,0) 70%, rgba(235,230,225,0.9) 78%, #e6e4e2 100%),
      linear-gradient(180deg, #c9d1d8 0%, #b4553a 35%, #9b3f2a 70%, #6d3326 100%);
  }
  .hero-title {
    position: absolute; left: 311px; top: 232px; width: 578px; height: 59px;
    background: var(--overlay); color: #fff; text-align: center;
    font-family: "Open Sans", sans-serif; font-size: 44px; line-height: 58px;
  }
  .hero-lead {
    position: absolute; left: 185px; top: 304px; width: 830px; height: 88px;
    background: var(--overlay); color: #fff; text-align: center;
    font-family: "Open Sans", sans-serif; font-size: 29px; line-height: 36px;
    padding-top: 7px;
  }
  .hero-button {
    position: absolute; left: 483px; top: 405px; width: 214px; height: 60px;
    border: 2px solid var(--ink);
    display: flex; align-items: center; justify-content: center;
  }
  .hero-button span {
    width: 200px; height: 47px; background: var(--brand-yellow);
    font-family: "Open Sans", sans-serif; font-size: 23px; line-height: 47px;
    text-align: center; color: var(--ink);
  }

  /* Content panel */
  .tab {
    position: absolute; top: 606px; height: 31px;
    font-family: "Open Sans", sans-serif; font-size: 18px; line-height: 31px;
    padding-left: 12px;
  }
  .tab-about { left: 100px; width: 245px; background: var(--brand-yellow); color: var(--ink); }
  .tab-projects { left: 608px; width: 245px; background: var(--brand-blue); color: #fff; }
  .content-panel {
    position: absolute; left: 100px; top: 637px; width: 1002px; height: 195px;
    background: var(--panel-white);
  }
  .column-divider {
    position: absolute; left: 507px; top: 0; width: 1px; height: 122px; background: var(--rule);
  }
  .about-text {
    position: absolute; left: 14px; top: 17px; width: 480px;
    font-size: 13px; line-height: 18px; color: var(--ink-soft);
  }
  .read-more {
    position: absolute; top: 89px; font-size: 14px; color: var(--ink);
  }
  .about-more { left: 14px; }
  .project-more { left: 522px; top: 90px; }
  .project-title {
    position: absolute; left: 522px; top: 17px; font-size: 14px; font-weight: 700; color: var(--ink);
    font-weight: 400;
  }
  .project-text {
    position: absolute; left: 522px; top: 38px; width: 230px;
    font-size: 13px; line-height: 18px; color: var(--ink-soft);
  }
  .project-photo {
    position: absolute; left: 758px; top: 10px; width: 230px; height: 101px;
    background: linear-gradient(180deg, #d5d8da 0%, #c9cdd0 45%, #8c8f86 70%, #5c6456 100%);
  }
  .panel-rule {
    position: absolute; left: 15px; top: 122px; width: 972px; height: 1px; background: var(--rule);
  }
  .client-row {
    position: absolute; left: 50px; top: 142px; width: 902px; height: 30px;
    display: flex; justify-content: space-between; align-items: center;
    font-family: "Open Sans", sans-serif; font-size: 15px; font-weight: 600; color: #3a3a3a;
    list-style: none;
  }

  /* Footer */
  .site-footer {
    position: absolute; left: 111px; top: 845px; width: 976px;
    display: flex; justify-content: space-between;
    font-size: 13px; color: var(--ink);
  }
</style>
</head>
<body>
  <header class="site-header">
    <a class="brand" href="#"><span class="brand-square"></span>Maple Ridge Ventures Ltd.</a>
    <p class="call-now">Call Now: <strong>0700 900 4182</strong></p>
    <nav class="main-nav">
      <a class="is-active" href="#">Home</a>
      <a href="#">About Us</a>
      <a href="#">Projects</a>
      <a href="#">Clients</a>
      <a href="#">Contact Us</a>
    </nav>
  </header>

  <div class="hero-photo" role="img" aria-label="Photograph of red-brick Victorian city buildings against a cloudy sky"></div>
  <h1 class="hero-title">‘It’s all about Attitude’</h1>
  <p class="hero-lead">Lorem Ipsum is simply dummy text of the printing and typesetting industry.</p>
  <a class="hero-button" href="#"><span>Project Details</span></a>

  <h2 class="tab tab-about">Who We Are</h2>
  <h2 class="tab tab-projects">Latest Projects:</h2>

  <section class="content-panel">
    <p class="about-text">Maple Ridge Ventures Ltd is a project management company that embraces a modern philosophy based on 40 years of in-house and consultancy client experience and expertise; latterly with involvement with a number of high end London projects.</p>
    <a class="read-more about-more" href="#">Read More →</a>
    <div class="column-divider"></div>
    <h3 class="project-title">Riverside Student Accommodation</h3>
    <p class="project-text">Lorem Ipsum is simply dummy text of the printing and typesetting industry.</p>
    <a class="read-more project-more" href="#">Read More →</a>
    <div class="project-photo" role="img" aria-label="Photograph of a modern student accommodation block beside a river"></div>
    <div class="panel-rule"></div>
    <ul class="client-row">
      <li>Halden</li>
      <li>Brixel</li>
      <li>Norvo</li>
      <li>Caffora</li>
      <li>Pelta</li>
      <li>Lumeo</li>
      <li>Trelling</li>
      <li>Vantra</li>
      <li>Kessler</li>
    </ul>
  </section>

  <footer class="site-footer">
    <span>Copyright © 2014 Maple Ridge Ventures Ltd | All Rights Reserved</span>
    <span>Home | About Us | Projects | Clients | Contact Us</span>
  </footer>
</body>
</html>
```